Machinery Instruction Manual

We need an instruction manual design that will be used as a template for all user manuals for our range of consumer machinery.
Our product range includes Chainsaws and Jackhammers for example.
======================
Essential:
======================
A staff member with only *Basic* Microsoft Word skills must be able to paste the required content from external sources in to the template to produce a professional manual.
The document should use the minimum amount of automated features.
Our staff need to produce manuals without hours of struggling with MS Word's "automated" features such as auto-bullets, auto-numbering, auto-indentation etc.
======================
The Design Should:
======================
- Be a Microsoft Word document, produced with Office 2013 or Office 365.
- Be suitable for production of printed manuals and online PDF manuals.
- Include the following sections:
1) Cover Page.
2) Approx 120 words of "warning text" (may be on cover or separate page).
3) Table Of Contents.
4) Body.
5) Specifications section featuring 3-10 different versions of the machine, each including a photo and listing approx 13 specifications.
- Include page numbers.
- Be in "Single Column Format" for easy editing by staff with minimal MS Word experience. "Special Pages", such as the cover and table of contents may be multi-column if necessary.
- Be an A4 document.
- Be readable when printed in Black and White, even if elements of the design include colour.
- Feature a warning icon/graphic that is easy to paste/insert next to important text.
- Feature the following levels of text, to be entered into MS Word's "Styles" function:
1) Main Headings.
2) Sub Headings.
3) Body Text.
- Feature headings that are "text", so they can be edited within MS Word without resorting to graphic editing software etc.
- Not rely on MS Word's painful "automated" features like auto-bullets, auto-numbering, auto-indentation etc (with the exception of page numbers, headings and auto-generated table of contents)
======================
How Our Staff Will Use It:
======================
Staff will have a basic understanding of MS Word.
Our staff will paste text, photographs, diagrams and vector drawings into the template.
======================
Extra Credit Given For:
======================
- Automatically generated table of contents, based on the headings within the document.
======================
Finished Template:
======================
- Should be in MS Word (MS Office 2013 or MS Office 365) format.
- Should include generic text / photos / diagrams to show what a manual looks like when generated from your template.
Project Deadline Extended
Reason: Following feedback, payment has been "committed".
Deadline extended to allow designers adequate time for production.

```html
<!DOCTYPE html>
<html lang="en">
<head>
<meta charset="utf-8">
<title>Jackhammars – Instruction Manual</title>
<link rel="stylesheet" href="https://fonts.googleapis.com/css2?family=Carlito:wght@400;700&display=swap">
<style>
  :root {
    --brand-blue: #1a7ff0;
    --section-tint: #c8ebf8;
    --text-ink: #111111;
    --heading-ink: #1d1d1d;
    --page-white: #ffffff;
  }
  * { box-sizing: border-box; margin: 0; padding: 0; }
  html, body {
    width: 1141px;
    height: 1200px;
    overflow: hidden;
    background: var(--page-white);
  }
  body {
    position: relative;
    font-family: "Carlito", "Calibri", sans-serif;
    color: var(--text-ink);
  }
  .page-header {
    position: absolute;
    left: 167px;
    top: 42px;
    width: 870px;
    height: 76px;
    background: var(--brand-blue);
    border-radius: 0 44px 18px 0;
  }
  .page-title {
    position: absolute;
    left: 8px;
    top: 16px;
    font-size: 39px;
    font-weight: 400;
    color: var(--page-white);
    letter-spacing: 0.5px;
  }
  .section { position: absolute; left: 167px; width: 908px; }
  .section-bar {
    height: 54px;
    background: var(--section-tint);
    display: flex;
    align-items: center;
    justify-content: center;
  }
  .section-heading {
    font-size: 31px;
    font-weight: 400;
    color: var(--heading-ink);
    letter-spacing: 0.5px;
  }
  .section-body {
    padding: 22px 38px 0 17px;
  }
  .body-text {
    font-size: 17.6px;
    line-height: 25px;
    margin-bottom: 11px;
  }
  .section--intro { top: 129px; }
  .section--history { top: 540px; }
  .section--use { top: 791px; }
  .page-number {
    position: absolute;
    left: 956px;
    top: 1094px;
    font-size: 17px;
    font-weight: 700;
  }
</style>
</head>
<body>
  <header class="page-header">
    <h1 class="page-title">JACKHAMMARS</h1>
  </header>

  <section class="section section--intro">
    <div class="section-bar"><h2 class="section-heading">INTRODUCTION</h2></div>
    <div class="section-body">
      <p class="body-text">A jackhammer (pneumatic drill or demolition hammer in British English) is a pneumatic or electro-mechanical tool that combines a hammer directly with a chisel. It was invented by Harold Pemberton Vance. Hand-held jackhammers are typically powered by compressed air, but some use electric motors. Larger jackhammers, such as rig mounted hammers used on construction machinery, are usually hydraulically powered. They are usually used to break up rock, pavement, and concrete.</p>
      <p class="body-text">A jackhammer operates by driving an internal hammer up and down. The hammer is first driven down to strike the back of the bit and then back up to return the hammer to the original position to repeat the cycle. The bit usually recovers from the stroke by means of a spring. The effectiveness of the jackhammer is dependent on how much force is applied to the tool.In British English electromechanical versions are colloquially known as "Thrumpers".</p>
    </div>
  </section>

  <section class="section section--history">
    <div class="section-bar"><h2 class="section-heading">HISTORY</h2></div>
    <div class="section-body">
      <p class="body-text">A jackhammer (pneumatic drill or demolition hammer in British English) is a pneumatic or electro-mechanical tool that combines a hammer directly with a chisel. It was invented by Harold Pemberton Vance. Hand-held jackhammers are typically powered by compressed air, but some use electric motors. Larger jackhammers, such as rig mounted hammers used on construction machinery, are usually hydraulically powered. They are usually used to break up rock, pavement, and concrete.</p>
    </div>
  </section>

  <section class="section section--use">
    <div class="section-bar"><h2 class="section-heading">USE</h2></div>
    <div class="section-body">
      <p class="body-text">A jackhammer (pneumatic drill or demolition hammer in British English) is a pneumatic or electro-mechanical tool that combines a hammer directly with a chisel. It was invented by Harold Pemberton Vance. Hand-held jackhammers are typically powered by compressed air, but some use electric motors. Larger jackhammers, such as rig mounted hammers used on construction machinery, are usually hydraulically powered. They are usually used to break up rock, pavement, and concrete.</p>
    </div>
  </section>

  <div class="page-number">1</div>
</body>
</html>
```